Project VELI

I am setting up a consultancy company in Istanbul, Turkey called VELI Partners. VELI partners will focus areas are highlighted in the attached presenatation. Expertise area as follows; Corporate Communications, Digitilization and Technology Integration, CSR & Sponsorships, Investor Relations and Fİnancial PR, Strategic Transactions, Corporate Governance... In related arease Project Management and Training support given.. For details see presenations. Our company collars are marun and blue.. In the attached presenations you can also see the business card colars and logo design. The design should reflect innovationi technology knowhow and power of communications skills. Enclosed you can find a presentations of scope of consultancy services and corporate logo from which logo and colars can be adapted..

Target Market(s)

Potential clients are any Holding or Company that would need services defined in the presantation attached.

Industry/Entity Type

It Company

Coding

Coded - Design and coding required

Number of Pages Required

5+ page

Font styles to use
Sans Serif

Requirements
Must have
• Main Expertize areas are defined in the presentation. The clients should be able to clearly see these and as they select the related area go to related page to see the content detail. I should be to also include vision statement in front page.. I should be able to present partners of the company in a related section. site should allow posting of pictures and an introductory video... Please use the logo and colars ı provided on attached file. Marun should be the dominating colar.
Nice to have
• www.morvanthrel.com I like.. Morvant provides somewhat similar services world wide. You can check out the site but don't need to necessarly do the same..

```html
<!DOCTYPE html>
<html lang="en">
<head>
<meta charset="utf-8">
<title>VELI Partners</title>
<link href="https://fonts.googleapis.com/css2?family=Open+Sans:wght@400;600;700&display=swap" rel="stylesheet">
<style>
:root{
  --maroon:#86124a;
  --maroon-dark:#6a0c39;
  --blue:#2d3192;
  --blue-band:#2a3590;
  --ink:#333;
  --muted:#8a8a8a;
  --canvas:#e9e9eb;
  --footer:#3d3d40;
  --footer-bottom:#2f2f31;
  --footer-text:#a9a9ad;
}
*{box-sizing:border-box;margin:0;padding:0}
html,body{width:710px;height:1200px;overflow:hidden}
body{background:var(--canvas);font-family:"Open Sans",Arial,sans-serif;color:var(--ink)}
.page{position:absolute;left:62px;top:0;width:590px;height:1172px;background:#fff;box-shadow:0 0 6px rgba(0,0,0,.12)}
.site-header{height:78px;display:flex;justify-content:space-between;align-items:center;padding:0 16px}
.brand{display:flex;align-items:center;gap:8px;font-weight:700;font-size:30px;color:var(--blue);letter-spacing:1px}
.brand-mark{width:14px;height:14px;background:var(--maroon);border-radius:50%}
.header-tools{display:flex;align-items:center;gap:4px}
.social-dot{width:12px;height:12px;border-radius:2px}
.login-btn{margin-left:8px;background:var(--maroon);color:#fff;font-size:8px;padding:4px 8px;border-radius:2px}
.main-nav{height:24px;background:linear-gradient(var(--maroon),var(--maroon-dark));display:flex;padding-left:12px}
.main-nav a{color:#fff;font-size:9px;text-decoration:none;padding:0 16px;line-height:24px}
.main-nav a.active{background:var(--blue)}
.hero{position:relative;margin:4px 0 0;height:238px;background:linear-gradient(135deg,#dfe3ea,#f4f5f7 45%,#c9cdd6)}
.hero-caption{position:absolute;left:160px;right:70px;top:202px;background:rgba(60,70,150,.55);color:#fff;font-size:11px;padding:5px 10px}
.intro{display:flex;gap:20px;padding:52px 20px 0}
.vision{flex:1}
.section-title{color:var(--blue);font-size:16px;font-weight:400;margin-bottom:8px}
.vision h3{font-size:9px;font-weight:700;margin-bottom:4px}
.vision p{font-size:7px;color:var(--muted);line-height:1.45}
.btn{display:inline-block;margin-top:14px;background:var(--maroon);color:#fff;font-size:8px;padding:6px 14px;border-radius:2px}
.video{width:236px}
.video-frame{height:118px;background:linear-gradient(135deg,#6a7080,#b9bdc6 50%,#4c5260);position:relative}
.video-bar{position:absolute;left:0;right:0;bottom:0;height:10px;background:rgba(0,0,0,.6)}
.expertise{padding-top:48px}
.expertise>h2{text-align:center;color:var(--maroon);font-size:15px;font-weight:400;margin-bottom:18px}
.expertise-grid{display:grid;grid-template-columns:repeat(3,1fr);gap:36px 24px;padding:0 26px}
.area{display:grid;grid-template-columns:24px 1fr;column-gap:10px}
.area-icon{width:22px;height:22px;background:var(--maroon);border-radius:3px;display:flex;align-items:center;justify-content:center}
.area h4{color:var(--maroon);font-size:9px;font-weight:700;line-height:1.25;align-self:center}
.area p{grid-column:1/3;font-size:6.5px;color:var(--muted);line-height:1.4;margin-top:6px}
.area a{grid-column:1/3;font-size:7px;color:var(--maroon);margin-top:6px;text-decoration:none}
.tweet-band{position:absolute;left:0;right:0;top:945px;height:45px;background:var(--blue-band);display:flex;align-items:center;justify-content:center;gap:10px;color:#fff;font-size:8px}
.tweet-dot{width:16px;height:16px;border-radius:50%;background:#fff;opacity:.85}
.site-footer{position:absolute;left:0;right:0;top:990px;height:160px;background:var(--footer);display:grid;grid-template-columns:1fr 1fr 1fr 1fr;gap:18px;padding:20px 20px 0;color:var(--footer-text);font-size:6.5px;line-height:1.5}
.footer-brand{font-size:26px;font-weight:700;color:#d5d5d8;margin-bottom:6px;display:flex;align-items:center;gap:6px}
.footer-brand span{width:10px;height:10px;background:var(--maroon);border-radius:50%}
.site-footer h5{color:#e4e4e6;font-size:7px;font-weight:700;letter-spacing:.4px;margin-bottom:8px}
.post{margin-bottom:8px}
.post b{color:#d5d5d8;font-weight:600}
.subscribe{display:flex;gap:4px;margin:6px 0 12px}
.subscribe span{flex:1;height:12px;background:#555}
.subscribe em{font-style:normal;background:#555;padding:1px 6px;color:#ddd}
.social-row{display:flex;gap:6px}
.social-row i{width:8px;height:8px;background:#8c8c90;border-radius:50%}
.footer-bottom{position:absolute;left:0;right:0;top:1150px;height:22px;background:var(--footer-bottom);color:#888;font-size:6.5px;display:flex;align-items:center;justify-content:center}
</style>
</head>
<body>
<div class="page">
  <header class="site-header">
    <div class="brand"><span class="brand-mark"></span>VELI</div>
    <div class="header-tools">
      <span class="social-dot" style="background:#3b5998"></span>
      <span class="social-dot" style="background:#d34836"></span>
      <span class="social-dot" style="background:#cb2027"></span>
      <span class="social-dot" style="background:#1da1f2"></span>
      <span class="login-btn">Login / Register</span>
    </div>
  </header>
  <nav class="main-nav">
    <a class="active">Home</a><a>About Us</a><a>ExpertiseAreas</a><a>Our Vision</a><a>Testimonials</a><a>Contact Us</a>
  </nav>
  <section class="hero" role="img" aria-label="Business team meeting around a presentation board">
    <div class="hero-caption">Lorem ipsum dolor sit amet consectetur adipiscing elit</div>
  </section>
  <section class="intro">
    <div class="vision">
      <h2 class="section-title">Our Vision</h2>
      <h3>Lorem ipsum dolor sit Contantry</h3>
      <p>Lorem ipsum dolor sit amet, consectetuer adipiscing elit. Maecenas porttitor congue massa. Fusce posuere, magna sed pulvinar ultricies, purus lectus malesuada libero, sit amet commodo magna eros quis urna. Nunc viverra imperdiet enim. Fusce est. Vivamus a tellus. Pellentesque habitant morbi tristique senectus et netus et malesuada fames ac turpis egestas. Proin pharetra nonummy pede. Mauris et orci. Aenean nec lorem.</p>
      <span class="btn">Read more</span>
    </div>
    <div class="video">
      <h2 class="section-title">Introductory video</h2>
      <div class="video-frame" role="img" aria-label="Introductory video still of a business meeting"><div class="video-bar"></div></div>
    </div>
  </section>
  <section class="expertise">
    <h2>Expertise Area's</h2>
    <div class="expertise-grid">
      <div class="area"><span class="area-icon"><svg width="12" height="12" viewBox="0 0 12 12"><rect x="1" y="2" width="10" height="7" rx="1" fill="#fff"/></svg></span><h4>Corporate Communications</h4><p>Etiam mattis eget magna at pellentesque. Sed euismod eget elit at posuere. Nulla maximus congue euismod.</p><a>Details</a></div>
      <div class="area"><span class="area-icon"><svg width="12" height="12" viewBox="0 0 12 12"><rect x="2" y="2" width="8" height="8" fill="none" stroke="#fff" stroke-width="1.5"/></svg></span><h4>Digitization and Technology Integration</h4><p>Etiam mattis eget magna at pellentesque. Sed euismod eget elit at posuere. Nulla maximus congue euismod.</p><a>Details</a></div>
      <div class="area"><span class="area-icon"><svg width="12" height="12" viewBox="0 0 12 12"><path d="M2 6l3 3 5-6" fill="none" stroke="#fff" stroke-width="1.6"/></svg></span><h4>CSR &amp; Sponsorships</h4><p>Etiam mattis eget magna at pellentesque. Sed euismod eget elit at posuere. Nulla maximus congue euismod.</p><a>Details</a></div>
      <div class="area"><span class="area-icon"><svg width="12" height="12" viewBox="0 0 12 12"><path d="M2 10V7M5 10V4M8 10V6M11 10V2" stroke="#fff" stroke-width="1.6"/></svg></span><h4>Investor Relations and Financial PR</h4><p>Etiam mattis eget magna at pellentesque. Sed euismod eget elit at posuere. Nulla maximus congue euismod.</p><a>Details</a></div>
      <div class="area"><span class="area-icon"><svg width="12" height="12" viewBox="0 0 12 12"><path d="M1 6h8M6 3l3 3-3 3" fill="none" stroke="#fff" stroke-width="1.6"/></svg></span><h4>Strategic Transactions</h4><p>Etiam mattis eget magna at pellentesque. Sed euismod eget elit at posuere. Nulla maximus congue euismod.</p><a>Details</a></div>
      <div class="area"><span class="area-icon"><svg width="12" height="12" viewBox="0 0 12 12"><circle cx="6" cy="6" r="4" fill="none" stroke="#fff" stroke-width="1.6"/></svg></span><h4>Corporate Governance</h4><p>Etiam mattis eget magna at pellentesque. Sed euismod eget elit at posuere. Nulla maximus congue euismod.</p><a>Details</a></div>
    </div>
  </section>
  <div class="tweet-band"><span class="tweet-dot"></span>@Lorem Because we know you don't want to be limited on a portrait or scape format ... by Quif</div>
  <footer class="site-footer">
    <div>
      <div class="footer-brand"><span></span>VELI</div>
      <p>Etiam mattis eget magna at pellentesque. Sed euismod eget elit at posuere. Nulla maximus congue euismod.</p>
    </div>
    <div>
      <h5>RECENT POSTS</h5>
      <p class="post">MAY 14, 2015 — <b>Mortis a libero eget erat auctor</b><br>Vel aliquet id tortor suspendisse.</p>
      <p class="post">MAY 02, 2015 — <b>Mortis a libero eget erat auctor</b><br>Vel aliquet id tortor suspendisse.</p>
    </div>
    <div>
      <h5>CONTACTS</h5>
      <p>VELI Partners<br>Halden Sok. No:12<br>Besiktas, Istanbul</p>
      <p style="margin-top:6px">Phone: +90 212 555 0147<br>Fax: +90 212 555 0148</p>
      <p style="margin-top:6px">hello@velipartners.com</p>
    </div>
    <div>
      <h5>NEWSLETTER SIGNUP</h5>
      <p>Lorem ipsum dolor sit amet, sign up for updates.</p>
      <div class="subscribe"><span></span><em>Join</em></div>
      <h5>GET SOCIAL</h5>
      <div class="social-row"><i></i><i></i><i></i><i></i><i></i></div>
    </div>
  </footer>
  <div class="footer-bottom">© 2015 VELI Partners. All Rights Reserved</div>
</div>
</body>
</html>
```